" Fazer o calendário de parede conforme o anexo abaixo sendo que a parte para fazer o cabeçalho tem que ter a medida 41cm de comprimento por 11,5cm de altura "

```html
<!DOCTYPE html>
<html lang="pt-BR">
<head>
<meta charset="utf-8">
<title>Calendário 2026 – Pomareal Hortifruti</title>
<link rel="stylesheet" href="https://fonts.googleapis.com/css2?family=Poppins:wght@400;500;600;700;800&display=swap">
<style>
  :root{
    --green:#2f8f4e;
    --green-dark:#1e7038;
    --green-soft:#cfe6d4;
    --ink:#262626;
    --muted:#6b6b6b;
    --paper:#ffffff;
    --bg:#eeeeec;
  }
  *{box-sizing:border-box;margin:0;padding:0}
  html,body{width:1200px;height:1200px;overflow:hidden;background:var(--bg)}
  body{font-family:"Poppins",sans-serif;color:var(--ink);position:relative}

  .calendar{
    position:absolute;left:190px;top:20px;width:820px;height:1160px;
    background:var(--paper);
    display:flex;flex-direction:column;
  }

  /* Header 41 x 11.5 cm */
  .header{
    position:relative;height:230px;flex:none;overflow:hidden;
    background:linear-gradient(90deg,#ffffff 0%,#ffffff 30%,#e3f1e6 45%,var(--green) 75%,var(--green-dark) 100%);
  }
  .header-photo{
    position:absolute;right:0;top:0;width:62%;height:100%;
    background:
      radial-gradient(ellipse at 55% 35%,rgba(120,190,110,.55),transparent 60%),
      radial-gradient(ellipse at 85% 70%,rgba(20,90,45,.45),transparent 65%),
      linear-gradient(90deg,rgba(255,255,255,0),rgba(60,140,80,.35));
  }
  .header-wave{position:absolute;left:0;bottom:0;width:100%;height:60px}
  .brand{position:absolute;left:38px;top:36px}
  .brand-name{
    display:flex;align-items:center;gap:12px;
    font-weight:800;font-size:34px;line-height:1;color:var(--green);
  }
  .brand-dot{width:26px;height:26px;border-radius:50%;background:var(--green);flex:none}
  .brand-address{margin-top:16px;font-size:12.5px;line-height:1.45;color:var(--muted);font-weight:500;padding-left:38px}

  .year-box{
    position:absolute;right:34px;top:70px;width:200px;height:112px;
    background:var(--green-dark);color:#fff;text-align:center;
    display:flex;flex-direction:column;justify-content:center;
  }
  .year{font-size:60px;font-weight:700;line-height:1;letter-spacing:1px}
  .year-label{font-size:14px;font-weight:500;letter-spacing:5px;margin-top:6px}

  /* Months */
  .months{
    flex:1;display:grid;grid-template-columns:repeat(3,1fr);grid-template-rows:repeat(4,1fr);
    column-gap:34px;row-gap:6px;padding:18px 34px 24px;
  }
  .month h2{font-size:15px;font-weight:700;color:var(--green);letter-spacing:.5px;margin-bottom:3px}
  .weekdays,.days{list-style:none;display:grid;grid-template-columns:repeat(7,1fr);text-align:center}
  .weekdays{font-size:9px;font-weight:600;color:var(--muted);border-bottom:1px solid var(--green-soft);padding-bottom:2px;margin-bottom:2px}
  .days{font-size:17px;font-weight:700;line-height:22px;color:var(--ink)}
  .days li:nth-child(7n+1){color:var(--green)}
  .days li.h{color:var(--green)}
  .note{font-size:8.5px;color:var(--muted);font-weight:500;margin-top:3px;text-align:right}
</style>
</head>
<body>
<article class="calendar">
  <header class="header">
    <div class="header-photo" role="img" aria-label="Fotografia suave de frutas e folhas verdes ao fundo"></div>
    <svg class="header-wave" viewBox="0 0 820 60" preserveAspectRatio="none" aria-hidden="true">
      <path d="M0 60 L0 40 C200 58 420 20 820 34 L820 60 Z" fill="#ffffff" opacity=".55"/>
    </svg>
    <div class="brand">
      <div class="brand-name"><span class="brand-dot"></span>Pomareal Hortifruti</div>
      <p class="brand-address">Av. das Palmeiras, 512 | Jardim Verde<br>Vila Aurora | VA</p>
    </div>
    <div class="year-box">
      <span class="year">2026</span>
      <span class="year-label">CALENDÁRIO</span>
    </div>
  </header>

  <main class="months">
    <section class="month"><h2>JANEIRO</h2>
      <ul class="weekdays"><li>D</li><li>S</li><li>T</li><li>Q</li><li>Q</li><li>S</li><li>S</li></ul>
      <ol class="days"><li></li><li></li><li></li><li></li><li class="h">1</li><li>2</li><li>3</li><li>4</li><li>5</li><li>6</li><li>7</li><li>8</li><li>9</li><li>10</li><li>11</li><li>12</li><li>13</li><li>14</li><li>15</li><li>16</li><li>17</li><li>18</li><li>19</li><li>20</li><li>21</li><li>22</li><li>23</li><li>24</li><li>25</li><li>26</li><li>27</li><li>28</li><li>29</li><li>30</li><li>31</li></ol>
      <p class="note">01 Ano Novo</p>
    </section>

    <section class="month"><h2>FEVEREIRO</h2>
      <ul class="weekdays"><li>D</li><li>S</li><li>T</li><li>Q</li><li>Q</li><li>S</li><li>S</li></ul>
      <ol class="days"><li>1</li><li>2</li><li>3</li><li>4</li><li>5</li><li>6</li><li>7</li><li>8</li><li>9</li><li>10</li><li>11</li><li>12</li><li>13</li><li>14</li><li>15</li><li>16</li><li class="h">17</li><li>18</li><li>19</li><li>20</li><li>21</li><li>22</li><li>23</li><li>24</li><li>25</li><li>26</li><li>27</li><li>28</li></ol>
      <p class="note">17 Carnaval</p>
    </section>

    <section class="month"><h2>MARÇO</h2>
      <ul class="weekdays"><li>D</li><li>S</li><li>T</li><li>Q</li><li>Q</li><li>S</li><li>S</li></ul>
      <ol class="days"><li>1</li><li>2</li><li>3</li><li>4</li><li>5</li><li>6</li><li>7</li><li>8</li><li>9</li><li>10</li><li>11</li><li>12</li><li>13</li><li>14</li><li>15</li><li>16</li><li>17</li><li>18</li><li>19</li><li>20</li><li>21</li><li>22</li><li>23</li><li>24</li><li>25</li><li>26</li><li>27</li><li>28</li><li>29</li><li>30</li><li>31</li></ol>
    </section>

    <section class="month"><h2>ABRIL</h2>
      <ul class="weekdays"><li>D</li><li>S</li><li>T</li><li>Q</li><li>Q</li><li>S</li><li>S</li></ul>
      <ol class="days"><li></li><li></li><li></li><li>1</li><li>2</li><li class="h">3</li><li>4</li><li>5</li><li>6</li><li>7</li><li>8</li><li>9</li><li>10</li><li>11</li><li>12</li><li>13</li><li>14</li><li>15</li><li>16</li><li>17</li><li>18</li><li>19</li><li>20</li><li class="h">21</li><li>22</li><li>23</li><li>24</li><li>25</li><li>26</li><li>27</li><li>28</li><li>29</li><li>30</li></ol>
      <p class="note">03 Sexta Santa · 21 Tiradentes</p>
    </section>

    <section class="month"><h2>MAIO</h2>
      <ul class="weekdays"><li>D</li><li>S</li><li>T</li><li>Q</li><li>Q</li><li>S</li><li>S</li></ul>
      <ol class="days"><li></li><li></li><li></li><li></li><li></li><li class="h">1</li><li>2</li><li>3</li><li>4</li><li>5</li><li>6</li><li>7</li><li>8</li><li>9</li><li>10</li><li>11</li><li>12</li><li>13</li><li>14</li><li>15</li><li>16</li><li>17</li><li>18</li><li>19</li><li>20</li><li>21</li><li>22</li><li>23</li><li>24</li><li>25</li><li>26</li><li>27</li><li>28</li><li>29</li><li>30</li><li>31</li></ol>
      <p class="note">01 Dia do Trabalho</p>
    </section>

    <section class="month"><h2>JUNHO</h2>
      <ul class="weekdays"><li>D</li><li>S</li><li>T</li><li>Q</li><li>Q</li><li>S</li><li>S</li></ul>
      <ol class="days"><li></li><li>1</li><li>2</li><li>3</li><li class="h">4</li><li>5</li><li>6</li><li>7</li><li>8</li><li>9</li><li>10</li><li>11</li><li>12</li><li>13</li><li>14</li><li>15</li><li>16</li><li>17</li><li>18</li><li>19</li><li>20</li><li>21</li><li>22</li><li>23</li><li>24</li><li>25</li><li>26</li><li>27</li><li>28</li><li>29</li><li>30</li></ol>
      <p class="note">04 Corpus Christi</p>
    </section>

    <section class="month"><h2>JULHO</h2>
      <ul class="weekdays"><li>D</li><li>S</li><li>T</li><li>Q</li><li>Q</li><li>S</li><li>S</li></ul>
      <ol class="days"><li></li><li></li><li></li><li>1</li><li>2</li><li>3</li><li>4</li><li>5</li><li>6</li><li>7</li><li>8</li><li>9</li><li>10</li><li>11</li><li>12</li><li>13</li><li>14</li><li>15</li><li>16</li><li>17</li><li>18</li><li>19</li><li>20</li><li>21</li><li>22</li><li>23</li><li>24</li><li>25</li><li>26</li><li>27</li><li>28</li><li>29</li><li>30</li><li>31</li></ol>
    </section>

    <section class="month"><h2>AGOSTO</h2>
      <ul class="weekdays"><li>D</li><li>S</li><li>T</li><li>Q</li><li>Q</li><li>S</li><li>S</li></ul>
      <ol class="days"><li></li><li></li><li></li><li></li><li></li><li></li><li>1</li><li>2</li><li>3</li><li>4</li><li>5</li><li>6</li><li>7</li><li>8</li><li>9</li><li>10</li><li>11</li><li>12</li><li>13</li><li>14</li><li>15</li><li>16</li><li>17</li><li>18</li><li>19</li><li>20</li><li>21</li><li>22</li><li>23</li><li>24</li><li>25</li><li>26</li><li>27</li><li>28</li><li>29</li><li>30</li><li>31</li></ol>
    </section>

    <section class="month"><h2>SETEMBRO</h2>
      <ul class="weekdays"><li>D</li><li>S</li><li>T</li><li>Q</li><li>Q</li><li>S</li><li>S</li></ul>
      <ol class="days"><li></li><li></li><li>1</li><li>2</li><li>3</li><li>4</li><li>5</li><li>6</li><li class="h">7</li><li>8</li><li>9</li><li>10</li><li>11</li><li>12</li><li>13</li><li>14</li><li>15</li><li>16</li><li>17</li><li>18</li><li>19</li><li>20</li><li>21</li><li>22</li><li>23</li><li>24</li><li>25</li><li>26</li><li>27</li><li>28</li><li>29</li><li>30</li></ol>
      <p class="note">07 Independência</p>
    </section>

    <section class="month"><h2>OUTUBRO</h2>
      <ul class="weekdays"><li>D</li><li>S</li><li>T</li><li>Q</li><li>Q</li><li>S</li><li>S</li></ul>
      <ol class="days"><li></li><li></li><li></li><li></li><li>1</li><li>2</li><li>3</li><li>4</li><li>5</li><li>6</li><li>7</li><li>8</li><li>9</li><li>10</li><li>11</li><li class="h">12</li><li>13</li><li>14</li><li>15</li><li>16</li><li>17</li><li>18</li><li>19</li><li>20</li><li>21</li><li>22</li><li>23</li><li>24</li><li>25</li><li>26</li><li>27</li><li>28</li><li>29</li><li>30</li><li>31</li></ol>
      <p class="note">12 Nossa Senhora</p>
    </section>

    <section class="month"><h2>NOVEMBRO</h2>
      <ul class="weekdays"><li>D</li><li>S</li><li>T</li><li>Q</li><li>Q</li><li>S</li><li>S</li></ul>
      <ol class="days"><li>1</li><li class="h">2</li><li>3</li><li>4</li><li>5</li><li>6</li><li>7</li><li>8</li><li>9</li><li>10</li><li>11</li><li>12</li><li>13</li><li>14</li><li>15</li><li>16</li><li>17</li><li>18</li><li>19</li><li class="h">20</li><li>21</li><li>22</li><li>23</li><li>24</li><li>25</li><li>26</li><li>27</li><li>28</li><li>29</li><li>30</li></ol>
      <p class="note">02 Finados · 20 Consciência</p>
    </section>

    <section class="month"><h2>DEZEMBRO</h2>
      <ul class="weekdays"><li>D</li><li>S</li><li>T</li><li>Q</li><li>Q</li><li>S</li><li>S</li></ul>
      <ol class="days"><li></li><li></li><li>1</li><li>2</li><li>3</li><li>4</li><li>5</li><li>6</li><li>7</li><li>8</li><li>9</li><li>10</li><li>11</li><li>12</li><li>13</li><li>14</li><li>15</li><li>16</li><li>17</li><li>18</li><li>19</li><li>20</li><li>21</li><li>22</li><li>23</li><li>24</li><li class="h">25</li><li>26</li><li>27</li><li>28</li><li>29</li><li>30</li><li>31</li></ol>
      <p class="note">25 Natal</p>
    </section>
  </main>
</article>
</body>
</html>
```